Austrian finance und insurance broker needs business card design

We Need a serious looking Design for Business Card. we consult private and corporates customers in finance and insurance questions. the final design should express security and experience. We consult customers in questions of loans, Investments and insurance and have a wide range of Banks to offer. We compare several offers and select the best for our customers.

Target Market(s)

private and coporate customers with efforts in Money and insurance

Industry/Entity Type

Insurance Broker

Contact Information for Business Card

Martin Brauneder
Geschäftsführer
staatl. geprüfter Vermögensberater und Versicherungsmakler
Tel: 0664 512 8049
office@der-brauneder.at
www.der-brauneder.at
Anton Weibl Gasse 14
2135 Halbach
GISA Nr. 40527318 u. 40816493 (backside)

Font styles to use
Serif
Sans Serif

Requirements
Must have
• logo (designcrowd zip) and all Details
Nice to have
• makler logo design, maybe a 2 coloured Version is possible

```html
<!DOCTYPE html>
<html lang="de">
<head>
<meta charset="utf-8">
<title>Weitblick Vermögensberatung – Visitenkarte</title>
<link href="https://fonts.googleapis.com/css2?family=Quicksand:wght@500;600;700&display=swap" rel="stylesheet">
<style>
  :root {
    --blue: #2f5fc4;
    --blue-dark: #24489a;
    --black: #111214;
    --ink: #3a3a3c;
    --grey: #8a8c90;
    --white: #ffffff;
    --badge: #d8343c;
    --stage: #2a2c30;
  }
  * { margin: 0; padding: 0; box-sizing: border-box; }
  html, body { width: 1200px; height: 900px; overflow: hidden; }
  body {
    background: var(--stage);
    font-family: "Quicksand", sans-serif;
    position: relative;
  }
  .card {
    position: absolute;
    top: 295px;
    width: 540px;
    height: 310px;
    border-radius: 18px;
    overflow: hidden;
  }
  .card-front { left: 40px; background: var(--white); }
  .card-back { left: 620px; background: var(--black); }

  /* Front */
  .front-identity {
    position: absolute; top: 52px; left: 0; right: 0;
    display: flex; align-items: center; justify-content: center; gap: 12px;
  }
  .brand-dot {
    width: 40px; height: 40px; border-radius: 50%;
    border: 3px solid var(--blue);
  }
  .person-name { color: var(--blue); font-size: 32px; font-weight: 700; }
  .person-role {
    position: absolute; top: 112px; left: 0; right: 0;
    text-align: center; color: var(--ink); font-size: 15px; font-weight: 600; line-height: 22px;
  }
  .contact-icons {
    position: absolute; top: 182px; left: 0; right: 0;
    display: flex; justify-content: space-around; padding: 0 60px;
  }
  .contact-icons svg { width: 20px; height: 20px; fill: var(--blue); }
  .contact-line {
    position: absolute; top: 218px; left: 0; right: 0;
    text-align: center; color: var(--ink); font-size: 14px; font-weight: 600; white-space: nowrap;
  }
  .contact-line .sep { color: var(--grey); margin: 0 10px; }
  .front-band {
    position: absolute; left: 0; right: 0; bottom: 0; height: 38px; background: var(--blue);
  }

  /* Back */
  .back-shape { position: absolute; inset: 0; }
  .back-identity {
    position: absolute; top: 58px; left: 40px;
    display: flex; align-items: center; gap: 12px;
  }
  .back-brand { color: var(--blue); font-size: 30px; font-weight: 700; }
  .back-divider {
    position: absolute; top: 40px; left: 240px; width: 2px; height: 110px; background: var(--grey);
  }
  .back-company {
    position: absolute; top: 72px; left: 258px;
  }
  .company-name { color: var(--blue); font-size: 22px; font-weight: 700; }
  .company-tagline { color: var(--grey); font-size: 15px; font-weight: 600; margin-top: 4px; }
  .back-address {
    position: absolute; left: 0; right: 0; bottom: 16px;
    text-align: center; color: var(--black); font-size: 13px; font-weight: 700;
  }
</style>
</head>
<body>

<section class="card card-front" aria-label="Visitenkarte Vorderseite">
  <div class="front-identity">
    <span class="brand-dot"></span>
    <h1 class="person-name">Martin Brauneder</h1>
  </div>
  <p class="person-role">Geschäftsführer<br>staatl. geprüfter Vermögensberater und Versicherungsmakler</p>

  <div class="contact-icons">
    <svg viewBox="0 0 24 24" aria-label="E-Mail"><path d="M2 5h20v14H2z M3.5 6.5 12 13l8.5-6.5" fill="none" stroke="#2f5fc4" stroke-width="2"/></svg>
    <svg viewBox="0 0 24 24" aria-label="Telefon"><path d="M6.6 10.8a15 15 0 0 0 6.6 6.6l2.2-2.2c.3-.3.7-.4 1-.2 1.1.4 2.3.6 3.6.6.6 0 1 .4 1 1V20c0 .6-.4 1-1 1A17 17 0 0 1 3 4c0-.6.4-1 1-1h3.5c.6 0 1 .4 1 1 0 1.3.2 2.5.6 3.6.1.3 0 .7-.2 1z"/></svg>
    <svg viewBox="0 0 24 24" aria-label="Web"><circle cx="12" cy="12" r="9" fill="none" stroke="#2f5fc4" stroke-width="2"/><path d="M3 12h18M12 3c3 3 3 15 0 18M12 3c-3 3-3 15 0 18" fill="none" stroke="#2f5fc4" stroke-width="1.6"/></svg>
  </div>
  <p class="contact-line">office@der-brauneder.at<span class="sep">|</span>0664 512 8049<span class="sep">|</span>www.der-brauneder.at</p>
  <div class="front-band"></div>
</section>

<section class="card card-back" aria-label="Visitenkarte Rückseite">
  <svg class="back-shape" viewBox="0 0 540 310" aria-hidden="true">
    <path d="M0 252 H215 Q228 252 230 238 Q233 222 250 222 H290 Q307 222 310 238 Q312 252 325 252 H540 V310 H0 Z" fill="#2f5fc4"/>
    <circle cx="270" cy="243" r="16" fill="#d8343c"/>
    <circle cx="270" cy="243" r="11" fill="none" stroke="#f08a8e" stroke-width="1.5"/>
  </svg>
  <div class="back-identity">
    <span class="brand-dot"></span>
    <span class="back-brand">Weitblick</span>
  </div>
  <div class="back-divider"></div>
  <div class="back-company">
    <p class="company-name">Vermögensberatung GmbH</p>
    <p class="company-tagline">Finanzieren, Versichern, Vorsorgen</p>
  </div>
  <p class="back-address">Anton Weibl Gasse 14, 2135 Halbach, GISA Nr. 40527318 u. 40816493</p>
</section>

</body>
</html>
```